Coffee Bag Design for Tidewell Coffee

We’re excited to invite you to help us bring Tidewell Coffee to life on grocery store shelves with a design that embodies our mission of spreading goodness and creating a lasting impact. Tidewell Coffee represents warmth, positivity, and the power of small actions to create ripples of goodness. Each cup not only offers a rich, gourmet coffee experience but also gives back to the community, with $2 from each bag supporting local food banks.

To reflect this vision, we’d love for the design to feature a dark (greyish) blue as the base color to convey depth and quality, complemented by a vibrant light blue that will catch the eye and add energy. Tan or gold accents could add an elegant touch and a feeling of warmth. We are aiming for a look that feels uplifting and engaging, with simplicity and elegance, yet stands out amid other brands on the shelf.

I am attaching the dimension of the bag.

Other information that needs to be listed:
Ingredients: 100% Arabica Coffee
Net Wt. 12 oz. (340 g)
Roasted and distributed by:
Name
Address
email

Text on the back of the bag:
Tidewell Coffee is crafted with a belief that kindness and positivity can spread, touching countless lives with every sip. This gourmet blend delivers a rich taste experience while giving back, as $2 from each bag sold is donated to local food banks to help those in need. Enjoy the warmth and goodness in each cup, knowing you’re making a difference with every purchase.

Thank you!

```html
<!DOCTYPE html>
<html lang="en">
<head>
<meta charset="UTF-8">
<title>Tidewell Coffee – Costa Rica Bag Front</title>
<link href="https://fonts.googleapis.com/css2?family=Poppins:ital,wght@0,400;0,500;0,600;0,700;1,500;1,700&family=Archivo+Black&display=swap" rel="stylesheet">
<style>
  :root {
    --backdrop: #e48e6d;
    --navy: #17233f;
    --navy-deep: #0f1930;
    --ink: #1a2850;
    --sky: #3a9be0;
    --sky-deep: #1f6fb3;
    --gold: #dcbc62;
    --gold-soft: #f0d88c;
    --cream: #ebe5d3;
    --cup-brown: #7a4a2a;
  }
  * { box-sizing: border-box; margin: 0; padding: 0; }
  html, body { width: 1200px; height: 900px; overflow: hidden; }
  body {
    background: var(--backdrop);
    font-family: "Poppins", sans-serif;
    color: var(--ink);
    position: relative;
  }
  .bag-front {
    position: absolute;
    left: 375px; top: 110px;
    width: 450px; height: 680px;
    border-radius: 10px 10px 2px 2px;
    overflow: hidden;
  }
  .scallop-pattern {
    position: absolute; inset: 0;
    background: radial-gradient(circle at 50% 40%, #22345a 0%, var(--navy) 55%, var(--navy-deep) 100%);
  }
  .center-band {
    position: absolute; top: 0; bottom: 0;
    left: 143px; width: 162px;
    background: linear-gradient(180deg, var(--sky-deep) 0%, var(--sky) 35%, var(--sky-deep) 60%, var(--sky) 100%);
  }
  .gold-stripe { position: absolute; top: 0; bottom: 0; background: var(--gold); }
  .gold-stripe.outer-left { left: 136px; width: 6px; }
  .gold-stripe.inner-left { left: 148px; width: 2px; }
  .gold-stripe.inner-right { left: 298px; width: 2px; }
  .gold-stripe.outer-right { left: 306px; width: 6px; }

  .brand-oval {
    position: absolute;
    left: 116px; top: 120px;
    width: 216px; height: 168px;
    border-radius: 50%;
    background: var(--navy-deep);
    border: 2px solid var(--gold);
    box-shadow: 0 0 0 5px var(--navy-deep);
    display: flex; align-items: center; justify-content: center;
  }
  .brand-oval .brand-name {
    font-weight: 500; font-size: 22px; color: var(--gold-soft);
    letter-spacing: 0.5px;
  }

  .info-label {
    position: absolute;
    left: 70px; top: 408px;
    width: 307px; height: 209px;
    background: var(--cream);
  }
  .info-label::before, .info-label::after {
    content: ""; position: absolute; left: 0; right: 0; height: 4px;
    background:
      linear-gradient(-45deg, var(--cream) 3px, transparent 0),
      linear-gradient(45deg, var(--cream) 3px, transparent 0);
    background-size: 6px 6px;
    background-repeat: repeat-x;
  }
  .info-label::before { top: -4px; background-position: left bottom; }
  .info-label::after { bottom: -4px; transform: scaleY(-1); }

  .label-brand { position: absolute; left: 24px; top: 22px; font-weight: 600; font-size: 12px; }
  .label-origin-line { position: absolute; left: 127px; top: 43px; font-size: 9.5px; }
  .quality-seal {
    position: absolute; right: 14px; top: 8px;
    width: 40px; height: 40px; border-radius: 50%;
    border: 1.5px solid var(--ink);
  }
  .rule { position: absolute; background: var(--ink); }
  .rule.top { left: 24px; width: 261px; top: 58px; height: 1px; }
  .rule.mid { left: 24px; width: 261px; top: 150px; height: 1px; }
  .rule.bottom { left: 24px; width: 261px; top: 192px; height: 1px; }
  .rule.column { left: 124px; top: 150px; width: 1px; height: 42px; }

  .tasting-quote {
    position: absolute; left: 24px; top: 65px; width: 100px;
    font-size: 5.6px; font-style: italic; font-weight: 500;
    text-align: center; line-height: 1.35;
  }
  .origin-box {
    position: absolute; left: 127px; top: 59px; width: 156px; height: 48px;
    background: var(--navy-deep); color: var(--cream);
    display: flex; flex-direction: column; align-items: center; justify-content: center;
  }
  .origin-box .country { font-family: "Archivo Black", sans-serif; font-size: 17px; letter-spacing: 0.8px; line-height: 1.1; }
  .origin-box .farm { font-weight: 700; font-size: 8px; letter-spacing: 0.6px; }

  .side-tab {
    position: absolute; top: 108px; width: 13px; height: 40px;
    background: var(--navy-deep); color: var(--cream);
    display: flex; align-items: center; justify-content: center;
  }
  .side-tab span { transform: rotate(-90deg); font-size: 5.5px; letter-spacing: 0.5px; white-space: nowrap; }
  .side-tab.notes { left: 24px; }
  .side-tab.roast { left: 127px; }
  .notes-text {
    position: absolute; left: 40px; top: 116px; width: 84px;
    font-size: 7.4px; font-weight: 700; font-style: italic; text-align: center; line-height: 1.3;
  }
  .roast-scale {
    position: absolute; left: 143px; top: 110px; width: 142px;
    display: flex; justify-content: space-between;
  }
  .roast-step { width: 27px; display: flex; flex-direction: column; align-items: center; }
  .roast-step svg { width: 24px; height: 22px; }
  .roast-step .step-name { font-size: 4.2px; color: var(--cup-brown); text-align: center; line-height: 1.05; margin-top: 1px; }

  .product-form { position: absolute; left: 34px; top: 157px; font-size: 9.5px; line-height: 1.55; }
  .product-form b { font-weight: 700; }
  .process { position: absolute; left: 137px; top: 156px; font-size: 7.5px; font-weight: 700; line-height: 1.1; }
  .net-weight { position: absolute; right: 26px; top: 155px; text-align: right; font-weight: 700; }
  .net-weight .title { font-size: 9px; margin-right: 6px; }
  .net-weight .amount { font-size: 11px; margin-top: 3px; }
</style>
</head>
<body>
  <main class="bag-front">
    <div class="scallop-pattern" role="img" aria-label="Repeating navy scallop pattern with fine gold arcs"></div>
    <div class="center-band" role="img" aria-label="Light blue interlaced lattice pattern band"></div>
    <div class="gold-stripe outer-left"></div>
    <div class="gold-stripe inner-left"></div>
    <div class="gold-stripe inner-right"></div>
    <div class="gold-stripe outer-right"></div>

    <div class="brand-oval">
      <span class="brand-name">Tidewell Coffee</span>
    </div>

    <section class="info-label">
      <div class="label-brand">Tidewell Coffee</div>
      <div class="label-origin-line">100% Arabica Coffee</div>
      <div class="quality-seal"></div>
      <div class="rule top"></div>

      <p class="tasting-quote">“Fruity Aroma,Long Sweet Finish,Structured Acidity,Juicy And Silky Mouthfeel,Flavour Note of Apricot,Caramel,Mixed Berries And Chocolate”</p>

      <div class="origin-box">
        <span class="country">COSTA RICA</span>
        <span class="farm">HACIENDA LOMA CLARA</span>
      </div>

      <div class="side-tab notes"><span>NOTES</span></div>
      <p class="notes-text">Mixed Berries And Chocolate,Caramel</p>

      <div class="side-tab roast"><span>ROAST</span></div>
      <div class="roast-scale">
        <div class="roast-step">
          <svg viewBox="0 0 24 22"><path d="M10 1c-1 1 1 2 0 3" stroke="#7a4a2a" fill="none" stroke-width="0.8"/><path d="M3 8h15v4a7 7 0 0 1-15 0z" fill="none" stroke="#7a4a2a" stroke-width="1.4"/><path d="M18 9h2a2.5 2.5 0 0 1 0 5h-2" fill="none" stroke="#7a4a2a" stroke-width="1.4"/></svg>
          <span class="step-name">LIGHT</span>
        </div>
        <div class="roast-step">
          <svg viewBox="0 0 24 22"><path d="M10 1c-1 1 1 2 0 3" stroke="#7a4a2a" fill="none" stroke-width="0.8"/><path d="M3 8h15v4a7 7 0 0 1-15 0z" fill="none" stroke="#7a4a2a" stroke-width="1.4"/><path d="M18 9h2a2.5 2.5 0 0 1 0 5h-2" fill="none" stroke="#7a4a2a" stroke-width="1.4"/></svg>
          <span class="step-name">LIGHT<br>MEDIUM</span>
        </div>
        <div class="roast-step">
          <svg viewBox="0 0 24 22"><path d="M10 1c-1 1 1 2 0 3" stroke="#7a4a2a" fill="none" stroke-width="0.8"/><path d="M3 8h15v4a7 7 0 0 1-15 0z" fill="none" stroke="#7a4a2a" stroke-width="1.4"/><path d="M18 9h2a2.5 2.5 0 0 1 0 5h-2" fill="none" stroke="#7a4a2a" stroke-width="1.4"/></svg>
          <span class="step-name">MEDIUM</span>
        </div>
        <div class="roast-step">
          <svg viewBox="0 0 24 22"><path d="M10 1c-1 1 1 2 0 3" stroke="#7a4a2a" fill="none" stroke-width="0.8"/><path d="M3 8h15v4a7 7 0 0 1-15 0z" fill="#5a3218" stroke="#7a4a2a" stroke-width="1.4"/><path d="M18 9h2a2.5 2.5 0 0 1 0 5h-2" fill="none" stroke="#7a4a2a" stroke-width="1.4"/></svg>
          <span class="step-name">MEDIUM<br>DARK</span>
        </div>
        <div class="roast-step">
          <svg viewBox="0 0 24 22"><path d="M10 1c-1 1 1 2 0 3" stroke="#7a4a2a" fill="none" stroke-width="0.8"/><path d="M3 8h15v4a7 7 0 0 1-15 0z" fill="none" stroke="#7a4a2a" stroke-width="1.4"/><path d="M18 9h2a2.5 2.5 0 0 1 0 5h-2" fill="none" stroke="#7a4a2a" stroke-width="1.4"/></svg>
          <span class="step-name">DARK</span>
        </div>
      </div>

      <div class="rule mid"></div>
      <div class="rule column"></div>

      <div class="product-form"><b>Roasted</b> coffee<br><b>Whole</b> bean</div>
      <div class="process">Traditional<br>Natural<br>Method</div>
      <div class="net-weight">
        <div class="title">Net Wt.</div>
        <div class="amount">12 oz. (340 g)</div>
      </div>

      <div class="rule bottom"></div>
    </section>
  </main>
</body>
</html>
```